Home Based Business Website Design

Need 1 template web design. Require clean friendly website design that helps promote a work from home business opportunity based around personal development. The site should lean towards appealing to the female market (see target market) and be straight forward, fresh colours and good use of white space. The site should have a family focus using imagery of happy families and reinforcing the quality of life and freedom available. The site should be in a two or three column format, navigation can be top or left, there will be 6 menu items in total (E.g. home, about, testimonials, contact, faq, why me?). There should be space for a video, text, images and a clear "call to action" (contact us). The site should come across as professiona, positive, friendly and trustworthy. Scope for many more sites of this nature in the future.

Target Market(s)

People that are ready for change. People wanting to make money from a business at home. 25+ years old, mum's , professional. People that are tired of the commute and want a better quality of life. While the site should lean towards focusing on stay at home mums or working mums looking for a better life it should also be able to appeal to a wider audience (male and female) so should not be too "girly"!

Industry/Entity Type

Business

Requirements
Must have
• Fairly open to interpretation, site must have at least two columns, clear call to action, space for a video, text and images, navigation (single level 6 items).
Nice to have
• Possibly animated banner of images?
Should not have
• Try to use less obvious imagery no stressed out executives or people jumping for joy. no dark designs no purple or flouro colours. Site should be modern in design.

```html
<!DOCTYPE html>
<html lang="en">
<head>
<meta charset="utf-8">
<title>Home Based Business – Welcome</title>
<link rel="stylesheet" href="https://fonts.googleapis.com/css2?family=Arimo:wght@400&display=swap">
<style>
  :root {
    --stage-top: #6e7073;
    --stage-bottom: #c6c7c9;
    --white: #ffffff;
    --aqua-light: #b3dfe6;
    --aqua-band: rgba(190, 228, 234, 0.85);
    --aqua-band-top: rgba(170, 218, 228, 0.7);
    --sky-top: #6fb2ea;
    --sky-bottom: #cfe6f6;
    --swoosh: #1b9ed8;
    --nav-top: #4fb6df;
    --nav-bottom: #93d2ea;
    --nav-line: #3aa6d3;
    --accent: #1ea4d6;
    --text: #3b3b3b;
    --photo-warm: #c9a27c;
  }
  * { box-sizing: border-box; margin: 0; padding: 0; }
  html, body { width: 1200px; height: 747px; overflow: hidden; }
  body {
    background: linear-gradient(var(--stage-top), var(--stage-bottom));
    font-family: "Arimo", Arial, sans-serif;
    position: relative;
  }
  .site {
    position: absolute; left: 117px; top: 70px;
    width: 969px; height: 605px;
    background: var(--aqua-light);
    box-shadow: 0 0 14px rgba(0,0,0,0.25);
    overflow: hidden;
  }
  .brand-cell {
    position: absolute; left: 0; top: 0; width: 182px; height: 243px;
    background: var(--white);
  }
  .brand-mark {
    position: absolute; left: 37px; top: 31px; width: 103px; height: 102px;
    border-radius: 13px;
    background: linear-gradient(135deg, #5bbce3, #9fd8ec);
    color: var(--white); font-size: 31px;
    display: flex; align-items: center; justify-content: center;
  }
  .hero {
    position: absolute; left: 182px; top: 0; width: 787px; height: 241px;
    background: linear-gradient(160deg, var(--sky-top), var(--sky-bottom) 70%, #e9eef2);
  }
  .hero-swoosh { position: absolute; left: 182px; top: 0; }
  .header-band {
    position: absolute; left: 0; top: 187px; width: 969px; height: 54px;
    background: linear-gradient(var(--aqua-band-top) 0 18px, var(--aqua-band) 18px);
  }
  .main-nav {
    position: absolute; left: 0; top: 243px; width: 182px; list-style: none;
  }
  .main-nav li {
    height: 36px; margin-bottom: 0;
    background: linear-gradient(var(--nav-top), var(--nav-bottom));
    border-bottom: 1px solid var(--nav-line);
    color: var(--white); font-size: 18px; line-height: 36px;
    padding-left: 22px; text-transform: uppercase;
  }
  .content {
    position: absolute; left: 182px; top: 243px; width: 545px; height: 362px;
    background: var(--white);
    padding: 20px 22px 0 22px;
  }
  .content h1 {
    font-weight: 400; font-size: 28px; color: var(--accent);
    margin-bottom: 12px; letter-spacing: -0.2px;
  }
  .content p {
    font-size: 12.4px; line-height: 15.9px; color: var(--text);
    width: 498px; margin-bottom: 15px;
  }
  .card {
    position: absolute; left: 738px; width: 217px;
    background: var(--white); border-radius: 14px;
  }
  .cta { top: 243px; height: 95px; display: flex; align-items: center; padding-left: 12px; }
  .cta-icon { width: 66px; height: 66px; }
  .cta-label { color: var(--accent); font-size: 19px; margin-left: 10px; }
  .video { top: 358px; height: 154px; }
  .video-frame {
    position: absolute; left: 6px; top: 9px; width: 206px; height: 112px;
    border-radius: 12px;
    background: linear-gradient(120deg, #e6ecef, var(--photo-warm) 55%, #d8dde0);
  }
  .video-play {
    position: absolute; right: 14px; bottom: 9px;
    display: flex; align-items: center; font-size: 13px; color: var(--text);
  }
  .video-play svg { margin-right: 6px; }
</style>
</head>
<body>
  <div class="site">
    <div class="hero" role="img" aria-label="Mother and daughter smiling with arms outstretched under a bright blue sky"></div>
    <svg class="hero-swoosh" width="787" height="241" viewBox="0 0 787 241" aria-hidden="true">
      <path d="M170 241 Q620 225 787 60 L787 110 Q640 241 330 241 Z" fill="var(--swoosh)"/>
      <path d="M120 241 Q600 230 787 40 L787 62 Q620 226 170 241 Z" fill="#ffffff" opacity="0.55"/>
    </svg>
    <div class="brand-cell">
      <div class="brand-mark">logo</div>
    </div>
    <div class="header-band"></div>

    <ul class="main-nav">
      <li>Home</li>
      <li>About</li>
      <li>Testimonials</li>
      <li>Contact</li>
      <li>FAQ</li>
      <li>Why me</li>
    </ul>

    <main class="content">
      <h1>welcome</h1>
      <p>Lorem ipsum dolor sit amet, consectetur adipiscing elit. Curabitur fringilla turpis id sapien viverra et facilisis enim luctus. Suspendisse interdum dapibus dignissim. Fusce scelerisque faucibus ornare. Morbi feugiat nisl sit amet mi sollicitudin semper. Morbi accumsan viverra justo, eu sagittis quam sagittis id. Praesent justo eros, tempor nec pulvinar ut, vulputate dictum mi. Suspendisse scelerisque quam a augue vestibulum vehicula. Aenean dictum ullamcorper leo, vel pretium nulla pulvinar vel. Sed turpis velit, vehicula sed pulvinar eget, posuere nec urna. Suspendisse sed lacus at augue commodo dignissim. In luctus fermentum tellus.</p>
      <p>Aenean luctus, arcu non laoreet hendrerit, mi erat gravida eros, et ornare ligula arcu id diam. Quisque interdum sollicitudin neque, in porta sapien dictum eu. Phasellus leo ante, auctor vel varius in, condimentum eu nisi. Suspendisse congue sem sit amet lectus fermentum non condimentum risus hendrerit. Vivamus mi lacus, ullamcorper at pretium id, blandit vitae sem. Praesent a mi id elit posuere eleifend. Nunc interdum ligula a mi pharetra hendrerit. Morbi aliquet mi eget dui pretium pharetra. Mauris et interdum felis. Sed elit lectus, pulvinar in mollis in, ullamcorper quis arcu. Proin diam erat, laoreet sed ornare vitae, ullamcorper quis justo.</p>
    </main>

    <aside>
      <div class="card cta">
        <svg class="cta-icon" viewBox="0 0 66 66" aria-hidden="true">
          <circle cx="33" cy="33" r="32" fill="#5bbce3"/>
          <circle cx="33" cy="33" r="25" fill="#8fd0ea" stroke="#ffffff" stroke-width="2"/>
          <path d="M20 28 Q20 21 33 21 Q46 21 46 28 L41 30 L40 26 Q33 24 26 26 L25 30 Z" fill="#ffffff"/>
          <path d="M24 31 L42 31 L45 44 L21 44 Z" fill="#ffffff"/>
          <g fill="#5bbce3">
            <rect x="27" y="34" width="3" height="2"/><rect x="32" y="34" width="3" height="2"/><rect x="37" y="34" width="3" height="2"/>
            <rect x="27" y="38" width="3" height="2"/><rect x="32" y="38" width="3" height="2"/><rect x="37" y="38" width="3" height="2"/>
          </g>
        </svg>
        <span class="cta-label">call to action</span>
      </div>

      <div class="card video">
        <div class="video-frame" role="img" aria-label="Video still of a mother and child at a laptop in a kitchen"></div>
        <div class="video-play">
          <svg width="20" height="20" viewBox="0 0 20 20" aria-hidden="true">
            <circle cx="10" cy="10" r="9.5" fill="#1f2a33"/>
            <circle cx="10" cy="10" r="7" fill="#2a8fd0"/>
            <path d="M8 6 L14 10 L8 14 Z" fill="#ffffff"/>
          </svg>
          play
        </div>
      </div>
    </aside>
  </div>
</body>
</html>
```